Atelier Marrow Architecture business card

We need to update our business card. We do high end custom residential, hospitality, and wellness architecture. We focus on creating unique spaces and design around the five senses, believing that architecture's true impact is not on our surroundings, but within us. We would like to see designs are instill a sense of calm awe. They should be crisp, fresh, clean, authentic, & contemporary without being sterile, overworked, or harsh. White space is important. Alternative materials are an option if natural. We have created our own logo and would like designs to incorporate it. However, we are willing to see alternatives if the logo becomes a stumbling block and you have an alternate you suggest. Card must have the following information:
Atelier Marrow Architecture, Inc.
728 Holloway Ct. NE Atlanta, GA 30318
Marcus T. Whitcombe, AIA, NCARB, LEED AP BD+C
ateliermarrow.example

Target Market(s)

Higher net worth individuals with an appreciation for design, nature, sustainability,

Industry/Entity Type

Architect

Contact Information for Business Card

See above. The title of Owner or Architect is helpful but not necessary. Minimalism should trump additional information.

Font styles to use
Serif
Sans Serif

Requirements
Must have
• It should look professional. It must use logo
Should not have
• caligraphy, animals, anything that is cute,

```html
<!DOCTYPE html>
<html lang="en">
<head>
<meta charset="utf-8">
<title>Atelier Marrow Architecture – Business Card</title>
<link rel="stylesheet" href="https://fonts.googleapis.com/css2?family=Noto+Serif:wght@400;700&display=swap">
<style>
  :root {
    --bg: #e6e6e4;
    --card: #ffffff;
    --green: #1b7a2c;
    --green-dark: #14661f;
    --ink: #3a3a3a;
    --muted: #666666;
    --rule: #dddddd;
    --charcoal: #3c3c3c;
  }
  * { margin: 0; padding: 0; box-sizing: border-box; }
  html, body {
    width: 1200px; height: 1000px; overflow: hidden;
    background: var(--bg);
    font-family: "Noto Serif", Georgia, serif;
  }
  .stage { position: relative; width: 1200px; height: 1000px; }

  .card {
    position: absolute; left: 220px; width: 760px;
    background: var(--card);
    border-radius: 30px;
    overflow: hidden;
    box-shadow: 0 2px 6px rgba(0,0,0,.12);
  }
  .card--front { top: 50px; height: 432px; }
  .card--back { top: 525px; height: 435px; }

  /* Front */
  .brand-name {
    position: absolute;
    color: var(--ink);
    font-weight: 400;
    text-transform: uppercase;
    line-height: 1.25;
  }
  .card--front .brand-name {
    left: 0; right: 0; top: 180px;
    text-align: center;
    font-size: 34px; letter-spacing: 8px;
  }
  .card--front .brand-name .mark {
    display: inline-block; width: 10px; height: 10px;
    background: var(--green); margin-left: 12px; vertical-align: middle;
  }
  .front-url {
    position: absolute; left: 0; right: 0; top: 366px;
    text-align: center; color: var(--green); font-size: 15px;
  }

  /* Back */
  .brush-area {
    position: absolute; left: 375px; top: 42px; width: 125px; height: 145px;
    border-radius: 18px;
    background: linear-gradient(135deg, #23893a, var(--green-dark));
  }
  .card--back .brand-name {
    right: 42px; top: 92px;
    text-align: right;
    font-size: 19px; letter-spacing: 4px;
  }
  .tab {
    position: absolute; left: 0; top: 210px; width: 12px; height: 40px;
    background: var(--green); border-radius: 0 6px 6px 0;
  }
  .person-name {
    position: absolute; left: 44px; top: 206px;
    color: var(--green); font-size: 21px; font-weight: 700;
  }
  .credentials {
    position: absolute; left: 44px; top: 236px;
    color: var(--muted); font-size: 15px; letter-spacing: .3px;
  }
  .divider {
    position: absolute; left: 44px; right: 42px; top: 270px;
    height: 1px; background: var(--rule);
  }
  .contact-list {
    position: absolute; left: 44px; top: 286px;
    list-style: none; color: var(--muted); font-size: 15.5px;
  }
  .contact-list li { display: flex; align-items: center; height: 22px; }
  .contact-list svg { width: 13px; height: 13px; margin-right: 9px; fill: var(--green); }
  .company {
    position: absolute; right: 42px; top: 305px;
    text-align: right; color: var(--muted); font-size: 15.5px; line-height: 22px;
  }
  .company strong { color: var(--green); font-weight: 700; }
  .footer-rule {
    position: absolute; left: 0; right: 0; top: 398px; height: 3px; background: var(--charcoal);
  }
  .footer-band {
    position: absolute; left: 0; right: 0; top: 406px; height: 29px;
    background: linear-gradient(180deg, #23893a, var(--green-dark));
  }
</style>
</head>
<body>
<main class="stage">

  <section class="card card--front" aria-label="Card front">
    <div class="brand-name">Atelier Marrow Architecture<span class="mark"></span></div>
    <div class="front-url">www.ateliermarrow.example</div>
  </section>

  <section class="card card--back" aria-label="Card back">
    <div class="brush-area" role="img" aria-label="Green brush-stroke texture behind the studio name"></div>
    <div class="brand-name">Atelier Marrow<br>Architecture</div>

    <div class="tab"></div>
    <h1 class="person-name">Marcus T. Whitcombe</h1>
    <p class="credentials">AIA, NCARB, LEED AP BD+C</p>
    <div class="divider"></div>

    <ul class="contact-list">
      <li><svg viewBox="0 0 16 16"><path d="M3.6 1.5l2.3 2.6-1.3 1.7c.9 1.9 2.4 3.5 4.4 4.5l1.6-1.3 2.7 2.2-1.3 2.4C7 13.2 2.4 8.6 1.6 3z"/></svg>404.555.0184</li>
      <li><svg viewBox="0 0 16 16"><path d="M4 1h8v4H4zM1 6h14v6h-3v3H4v-3H1zm4 4v4h6v-4z"/></svg>404.555.0147</li>
      <li><svg viewBox="0 0 16 16"><path d="M1 3h14v10H1zm1.5 1.2v.4L8 8.6l5.5-4V4.2z"/></svg>info@ateliermarrow.example</li>
      <li><svg viewBox="0 0 16 16"><path d="M8 1a7 7 0 100 14A7 7 0 008 1zm0 1.5c.8 0 1.7 1.5 2 3.5H6c.3-2 1.2-3.5 2-3.5zM2.6 6.5h2.2a11 11 0 000 3H2.6a5.5 5.5 0 010-3zm3.7 0h3.4a10 10 0 010 3H6.3a10 10 0 010-3zm4.9 0h2.2a5.5 5.5 0 010 3h-2.2a11 11 0 000-3zM6 10.5h4c-.3 2-1.2 3-2 3s-1.7-1-2-3z"/></svg>www.ateliermarrow.example</li>
    </ul>

    <address class="company" style="font-style:normal">
      <strong>Atelier Marrow Architecture, Inc.</strong><br>
      728 Holloway Ct. NE<br>
      Atlanta, GA 30318
    </address>

    <div class="footer-rule"></div>
    <div class="footer-band"></div>
  </section>

</main>
</body>
</html>
```